Webdesign für Steuerberaterin
Zielgruppe
Ich bin Steuerberaterin. Meine Zielgruppe sind sowohl Privatpersonen als auch Unternehmer sowie Männer und Frauen.
Aufgabenstellung
Bitte mein Logo und Foto mit berücksichtigen. Ich möchte keine Website, auf der alle 'Reiter' als eine Seite von oben nach unten durchlaufen. Sondern wirklich einzelne, voneinander getrennte Seiten.

```html
<!DOCTYPE html>
<html lang="de">
<head>
<meta charset="utf-8">
<title>Sabine Hortmann – Steuerberaterin</title>
<link href="https://fonts.googleapis.com/css2?family=Source+Sans+3:wght@400;600&family=Tinos&display=swap" rel="stylesheet">
<style>
  :root {
    --header-dark: #1c1a1f;
    --gold: #a8842a;
    --gold-light: #e0bb3c;
    --gold-deep: #c69d2c;
    --text: #555458;
    --line: #4a4a4a;
    --white: #ffffff;
    --portrait-light: #f1efec;
    --portrait-mid: #d9d5cf;
  }
  * { margin: 0; padding: 0; box-sizing: border-box; }
  html, body { width: 1200px; height: 1056px; overflow: hidden; background: var(--white); }
  .page { position: relative; width: 1200px; height: 1056px; font-family: "Source Sans 3", sans-serif; color: var(--text); }

  .site-header { position: absolute; left: 0; top: 0; width: 1200px; height: 217px; background: var(--header-dark); }

  .brand {
    position: absolute; left: 539px; top: 0; width: 182px; height: 179px;
    background: var(--white); z-index: 2;
    display: flex; flex-direction: column; align-items: center; justify-content: center; gap: 14px;
  }
  .brand-dot { width: 34px; height: 34px; border-radius: 50%; background: var(--header-dark); }
  .brand-name { font-size: 21px; font-weight: 400; color: var(--gold); letter-spacing: 0.3px; }

  .main-nav a {
    position: absolute; top: 240px; transform: translateX(-50%);
    color: var(--gold); text-decoration: none; font-size: 15px; line-height: 1;
  }
  .nav-about { left: 221px; }
  .nav-services { left: 315px; }
  .nav-contact { left: 902px; }
  .nav-imprint { left: 997px; }

  .portrait {
    position: absolute; left: 375px; top: 166px; width: 478px; height: 327px; z-index: 1;
    background: radial-gradient(ellipse at 50% 45%, var(--portrait-light) 0%, var(--portrait-mid) 100%);
  }

  .welcome { position: absolute; left: 0; top: 510px; width: 1226px; text-align: center; }
  .welcome-title {
    display: flex; align-items: center; justify-content: center; gap: 11px;
    font-family: "Tinos", serif; font-weight: 400; font-size: 25px; color: var(--gold); line-height: 40px;
  }
  .welcome-title::before, .welcome-title::after { content: ""; height: 1px; background: var(--line); }
  .welcome-title::before { width: 124px; }
  .welcome-title::after { width: 117px; }

  .welcome-lead { margin-top: 13px; font-size: 16px; font-weight: 600; line-height: 19.4px; }
  .welcome-text p { margin-top: 19.4px; font-size: 16px; line-height: 19.4px; }

  .site-footer {
    position: absolute; left: 0; top: 983px; width: 1200px; height: 73px;
    background: linear-gradient(to bottom, var(--gold-light), var(--gold-deep));
  }
</style>
</head>
<body>
<div class="page">
  <header class="site-header"></header>

  <div class="brand">
    <span class="brand-dot"></span>
    <span class="brand-name">Sabine Hortmann</span>
  </div>

  <nav class="main-nav">
    <a class="nav-about" href="#">Über mich</a>
    <a class="nav-services" href="#">Leistungen</a>
    <a class="nav-contact" href="#">Kontakt</a>
    <a class="nav-imprint" href="#">Impressum</a>
  </nav>

  <div class="portrait" role="img" aria-label="Porträtfoto der Steuerberaterin im dunklen Blazer vor heller Steinwand"></div>

  <main class="welcome">
    <h1 class="welcome-title">Schön, dass Sie da sind</h1>
    <p class="welcome-lead">Ich freue mich, dass Sie den Weg zu mir gefunden haben!</p>
    <div class="welcome-text">
      <p>Sie sind bei mir genau richtig:<br>
      Egal, ob Sie Privatperson sind, die Ihre Einkommensteuer-Erklärung<br>
      in vertrauensvolle Hände geben möchte,<br>
      oder Unternehmer, der sich z.B. das „Rundum-Sorglos-Paket“<br>
      mit Buchführung, Jahresabschluss und Steuererklärungen wünscht.</p>
      <p>Schauen Sie sich hier gerne um und melden Sie sich bei mir – ich bin bei jedem<br>
      steuerlichen Thema gerne Ihr kompetenter und zuverlässiger Ansprechpartner.</p>
      <p>Für mich ist es eine Selbstverständlichkeit,<br>
      dass ich auch nach mehr als 12 Jahren Berufserfahrung<br>
      durch permanente Fortbildungen immer auf dem aktuellsten Stand<br>
      der relevanten Gesetze und Verordnungen bin.<br>
      Nur so kann ich Sie bestmöglich beraten.</p>
    </div>
  </main>

  <footer class="site-footer"></footer>
</div>
</body>
</html>
```